Outdoor Company Business Card design

We are an outdoor adventure company needing a business card. We sell outdoor adventures and clothing. Please use our logo in the business card. We are looking for something unique but delivers a clear message as to who we are. Please be creative

Target Market(s)

Outdoor adventures

Industry/Entity Type

Business

Contact Information for Business Card

Business name: TrailBirch If using the logo, no need to have a spot for the name
Owner / CEO: Ross Dalby
Website: TrailBirch.example
Facebook: Facebook.com/TrailBirch
Instagram: @dalby_ross
phone number: 555-304-7192
Email: Dalbycrew@TrailBirch.example

Colors

Designer to choose colors to be used in the design.

Requirements
Must have
• The business card must include the details mentioned above. ie logo, my name, email, facebook, instagram, website, and phone number.
Should not have
• should not be cluttered or look messy

```html
<!DOCTYPE html>
<html lang="en">
<head>
<meta charset="utf-8">
<title>TrailBirch Business Card</title>
<link rel="stylesheet" href="https://fonts.googleapis.com/css2?family=Open+Sans:wght@400;600;700&display=swap">
<style>
  :root {
    --page: #e9ebef;
    --blue: #1a72c0;
    --blue-deep: #0d4f9c;
    --blue-dark: #0a3f80;
    --orange: #f0531c;
    --white: #ffffff;
    --ink-soft: #dbe8f6;
  }
  * { box-sizing: border-box; margin: 0; padding: 0; }
  html, body { width: 1200px; height: 900px; overflow: hidden; }
  body {
    background: var(--page);
    font-family: "Open Sans", sans-serif;
    display: flex;
    flex-direction: column;
    align-items: center;
    justify-content: center;
    gap: 50px;
  }
  .card {
    position: relative;
    width: 630px;
    height: 360px;
    border-radius: 26px;
    overflow: hidden;
    box-shadow: 0 10px 28px rgba(10, 40, 80, 0.18);
  }
  .card-front { background: var(--white); }
  .front-shapes { position: absolute; inset: 0; }

  .identity { position: absolute; left: 38px; top: 40px; color: var(--white); }
  .identity .name { font-size: 30px; font-weight: 700; letter-spacing: 0.2px; }
  .identity .role { font-size: 15px; font-weight: 400; margin-top: 2px; color: var(--ink-soft); }
  .socials { list-style: none; margin-top: 16px; font-size: 14px; }
  .socials li { display: flex; align-items: center; gap: 8px; margin-top: 4px; }
  .socials svg { width: 13px; height: 13px; flex: none; }

  .brand {
    display: flex;
    align-items: center;
    gap: 10px;
    font-weight: 700;
    letter-spacing: 1px;
    white-space: nowrap;
  }
  .brand .mark { border-radius: 50%; background: var(--orange); flex: none; }
  .card-front .brand { position: absolute; right: 40px; top: 80px; color: var(--blue); font-size: 34px; }
  .card-front .brand .mark { width: 24px; height: 24px; }

  .contact {
    position: absolute;
    right: 38px;
    bottom: 28px;
    list-style: none;
    color: var(--white);
    font-size: 17px;
    text-align: right;
  }
  .contact li { display: flex; align-items: center; justify-content: flex-end; gap: 10px; margin-top: 5px; }
  .contact svg { width: 15px; height: 15px; flex: none; }

  .card-back {
    background: radial-gradient(ellipse at 45% 40%, var(--blue) 0%, var(--blue-deep) 60%, var(--blue-dark) 100%);
    display: flex;
    flex-direction: column;
    align-items: center;
    justify-content: center;
  }
  .world-map {
    position: absolute;
    left: 40px; right: 30px; top: 30px; bottom: 30px;
    border-radius: 40%;
    background: radial-gradient(ellipse at center, rgba(255,255,255,0.12) 0%, rgba(255,255,255,0.04) 60%, rgba(255,255,255,0) 80%);
  }
  .card-back .brand { position: relative; color: var(--white); font-size: 40px; }
  .card-back .brand .mark { width: 28px; height: 28px; background: var(--white); }
  .card-back .site { position: relative; color: var(--white); font-size: 16px; margin-top: 26px; }
</style>
</head>
<body>

  <section class="card card-front">
    <svg class="front-shapes" viewBox="0 0 630 360" width="630" height="360" aria-hidden="true">
      <defs>
        <linearGradient id="waveBlue" x1="0" y1="0" x2="1" y2="1">
          <stop offset="0" stop-color="#1560ae"/>
          <stop offset="1" stop-color="#1b7ac8"/>
        </linearGradient>
      </defs>
      <path d="M0 0 H200 C270 0 270 120 370 160 C450 195 560 205 630 205 V360 H0 Z" fill="url(#waveBlue)"/>
      <path d="M192 -4 C238 4 256 40 272 72" fill="none" stroke="var(--orange)" stroke-width="7" stroke-linecap="round"/>
      <path d="M384 152 C462 182 560 192 634 192" fill="none" stroke="var(--orange)" stroke-width="7" stroke-linecap="round"/>
    </svg>

    <div class="identity">
      <p class="name">Ross Dalby</p>
      <p class="role">Owner / CEO</p>
      <ul class="socials">
        <li>
          <svg viewBox="0 0 12 12"><rect width="12" height="12" rx="2" fill="var(--orange)"/></svg>
          TrailBirch
        </li>
        <li>
          <svg viewBox="0 0 12 12"><circle cx="6" cy="6" r="6" fill="var(--orange)"/></svg>
          dalby_ross
        </li>
      </ul>
    </div>

    <div class="brand"><span class="mark"></span>TRAILBIRCH</div>

    <ul class="contact">
      <li>555-304-7192
        <svg viewBox="0 0 16 16"><path d="M4 1 L6.5 4.5 L5 6.5 C6 8.5 7.5 10 9.5 11 L11.5 9.5 L15 12 L13.5 15 C7 14.5 1.5 9 1 2.5 Z" fill="var(--orange)"/></svg>
      </li>
      <li>Dalbycrew@TrailBirch.example
        <svg viewBox="0 0 16 16"><rect x="1" y="3" width="14" height="10" rx="1.5" fill="var(--orange)"/><path d="M1.5 3.8 L8 9 L14.5 3.8" fill="none" stroke="var(--white)" stroke-width="1.3"/></svg>
      </li>
      <li>www.TrailBirch.example
        <svg viewBox="0 0 16 16"><circle cx="8" cy="8" r="7" fill="var(--orange)"/><path d="M1 8 H15 M8 1 C4 5 4 11 8 15 C12 11 12 5 8 1" fill="none" stroke="var(--white)" stroke-width="1"/></svg>
      </li>
    </ul>
  </section>

  <section class="card card-back">
    <div class="world-map" role="img" aria-label="Faint world map spread across the card background"></div>
    <div class="brand"><span class="mark"></span>TRAILBIRCH</div>
    <p class="site">www.TrailBirch.example</p>
  </section>

</body>
</html>
```